Banner Ads for Online Poker Promotion

We are an online poker network, the KVR (www.thekvr.eu). We are looking for a small selection of web banner ads for our latest promotion and we are trying crowdsourcing for the first time!

Banner sizes that we need are:
- 196x523 (static .psd and .png)
- 199x129 (static .psd and .png)
- 447x426 (static .psd and .png)
- 500x400 (static .psd and .png)
- 697x167 (static .psd and .png)
- 460x60 (animated .gif)

The promotion name is ‘Lucky Lap’ and the concept is that a person who enters one of the specified tournaments four or more times during the promotion will win a free ticket to play that tournament again. So effectively a ‘Loop Twice, Gain Extra Spin’ promo. We also are giving away €10,000 in free entries to the tournaments during the promotion. The specific tournaments are called ‘Quiet Dusk Up’ and ‘The Zeal Den’ and run daily on our network. The promotion runs October 1 – 31.

Guidelines:

The name of the promotion, ‘Lucky Lap’, should feature prominently in the banners.

The strap line can be ‘Loop Twice, Gain Extra Spin’ or something that encourages players to ‘take a shot’ at the tournaments.

Our network logo may feature, but is not absolutely necessary.

Examples of past promotional imagery can be found on our website, in particular these pages: http://www.thekvr.eu/promotions/ and http://www.thekvr.eu/promotions/archived-promotions/

We are looking to go in a more modern and risqué direction than the past, in order to stand out from competition which is very bland.

Please do not use common poker imagery – so no cards, chips, suit icons etc – or objects associated with live poker (tables, etc). This sort of imagery is too clichéd.

More like iOS7, less like iOS6

Think glamour, neon, rock music, extreme sports, and the Gilt Ledge!

If any further guidance is needed please don’t hesitate to ask.

```html
<!DOCTYPE html>
<html lang="en">
<head>
<meta charset="utf-8">
<title>Lucky Lap — Banner Set</title>
<link href="https://fonts.googleapis.com/css2?family=Oswald:wght@500;700&display=swap" rel="stylesheet">
<style>
  :root {
    --page: #ffffff;
    --banner-top: #2b2b2b;
    --banner-bottom: #161616;
    --neon-edge: #ff8a1a;
    --neon-glow: rgba(255, 120, 0, 0.85);
    --bulb: #ffc04a;
    --title-light: #ffe45a;
    --title-dark: #ff9a12;
    --logo: #444444;
    --cord: #0c0c0c;
  }
  * { box-sizing: border-box; margin: 0; padding: 0; }
  html, body {
    width: 1200px; height: 1200px; overflow: hidden;
    background: var(--page);
    font-family: "Oswald", "Arial Narrow", sans-serif;
  }
  .banner-set { position: relative; width: 1200px; height: 1200px; }

  .banner {
    position: absolute; overflow: hidden;
    background:
      linear-gradient(90deg, transparent 18%, var(--cord) 18.2%, transparent 18.5%, transparent 81.5%, var(--cord) 81.8%, transparent 82%),
      radial-gradient(ellipse at 50% 40%, var(--banner-top), var(--banner-bottom) 85%);
  }
  .banner--tall {
    background:
      linear-gradient(90deg, transparent 10%, var(--cord) 10.5%, transparent 11%, transparent 89%, var(--cord) 89.5%, transparent 90%),
      radial-gradient(ellipse at 50% 40%, var(--banner-top), var(--banner-bottom) 85%);
  }

  .sign { position: absolute; }
  .sign__shape {
    position: absolute; inset: 0; width: 100%; height: 100%; overflow: visible;
    filter: drop-shadow(0 0 6px var(--neon-glow)) drop-shadow(0 0 18px var(--neon-glow));
  }
  .sign__body { fill: url(#sign-fill); stroke: var(--neon-edge); stroke-width: 3; }
  .sign__bulbs { fill: none; stroke: var(--bulb); stroke-width: 3.2; stroke-linecap: round; stroke-dasharray: 0 9; }

  .sign__text {
    position: absolute; inset: 0;
    display: flex; flex-direction: column; align-items: center; justify-content: center;
    text-align: center; text-transform: uppercase; line-height: 1.05;
    filter: drop-shadow(0 0 6px var(--neon-glow));
  }
  .sign__title, .sign__tagline {
    background: linear-gradient(180deg, var(--title-light) 20%, var(--title-dark) 90%);
    -webkit-background-clip: text; background-clip: text;
    color: transparent; white-space: nowrap; font-weight: 700;
  }
  .sign__tagline { letter-spacing: -0.01em; }

  .network-name {
    position: absolute; color: var(--logo); font-weight: 500;
    letter-spacing: 0.04em; line-height: 1;
  }

  /* 697 x 167 */
  .banner--leaderboard { left: 45px; top: 22px; width: 835px; height: 199px; }
  .banner--leaderboard .sign { left: 150px; top: -6px; width: 536px; height: 211px; }
  .banner--leaderboard .sign__title { font-size: 56px; }
  .banner--leaderboard .sign__tagline { font-size: 30px; }
  .banner--leaderboard .network-name { left: 742px; top: 158px; font-size: 26px; }

  /* 196 x 523 */
  .banner--tall { left: 931px; top: 22px; width: 235px; height: 626px; }
  .banner--tall .sign { left: 4px; top: 240px; width: 227px; height: 160px; }
  .banner--tall .sign__title { font-size: 25px; }
  .banner--tall .sign__tagline { font-size: 12px; }
  .banner--tall .network-name { left: 0; right: 0; text-align: center; top: 90px; font-size: 40px; }

  /* 500 x 400 */
  .banner--rectangle { left: 22px; top: 257px; width: 598px; height: 477px; }
  .banner--rectangle .sign { left: 22px; top: 82px; width: 560px; height: 298px; }
  .banner--rectangle .sign__title { font-size: 74px; }
  .banner--rectangle .sign__tagline { font-size: 36px; }
  .banner--rectangle .network-name { left: 440px; top: 424px; font-size: 40px; }

  /* 447 x 426 */
  .banner--square { left: 651px; top: 669px; width: 535px; height: 507px; }
  .banner--square .sign { left: 22px; top: 108px; width: 492px; height: 272px; }
  .banner--square .sign__title { font-size: 66px; }
  .banner--square .sign__tagline { font-size: 32px; }
  .banner--square .network-name { left: 444px; top: 458px; font-size: 30px; }

  /* 199 x 129 */
  .banner--small { left: 343px; top: 825px; width: 238px; height: 153px; }
  .banner--small .sign { left: 6px; top: 12px; width: 226px; height: 132px; }
  .banner--small .sign__title { font-size: 25px; }
  .banner--small .sign__tagline { font-size: 12px; }
  .banner--small .network-name { right: 10px; bottom: 10px; font-size: 13px; }

  /* 460 x 60 */
  .banner--strip { left: 67px; top: 1106px; width: 552px; height: 72px; }
  .banner--strip .sign { left: 106px; top: -40px; width: 340px; height: 152px; }
  .banner--strip .sign__text {
    inset: auto; left: 0; right: 0; top: 40px; height: 72px;
    line-height: 1;
  }
  .banner--strip .sign__title { font-size: 28px; }
  .banner--strip .sign__tagline { font-size: 15px; margin-top: 2px; }
  .banner--strip .network-name { left: 490px; top: 42px; font-size: 16px; }
</style>
</head>
<body>
<svg width="0" height="0" style="position:absolute" aria-hidden="true">
  <defs>
    <radialGradient id="sign-fill" cx="50%" cy="50%" r="55%">
      <stop offset="0%" stop-color="#2a1a0c"/>
      <stop offset="100%" stop-color="#120c08"/>
    </radialGradient>
    <symbol id="neon-diamond" viewBox="0 0 100 100" preserveAspectRatio="none">
      <polygon class="sign__body" points="50,1 99,50 50,99 1,50" vector-effect="non-scaling-stroke"/>
      <polygon class="sign__bulbs" points="50,6 94,50 50,94 6,50" vector-effect="non-scaling-stroke"/>
    </symbol>
  </defs>
</svg>

<main class="banner-set">
  <section class="banner banner--leaderboard" aria-label="Banner 697 by 167">
    <div class="sign">
      <svg class="sign__shape" viewBox="0 0 100 100" preserveAspectRatio="none"><use href="#neon-diamond"/></svg>
      <div class="sign__text"><span class="sign__title">Lucky Lap</span><span class="sign__tagline">Loop Twice, Gain Extra Spin</span></div>
    </div>
    <span class="network-name">KVR</span>
  </section>

  <section class="banner banner--tall" aria-label="Banner 196 by 523">
    <span class="network-name">KVR</span>
    <div class="sign">
      <svg class="sign__shape" viewBox="0 0 100 100" preserveAspectRatio="none"><use href="#neon-diamond"/></svg>
      <div class="sign__text"><span class="sign__title">Lucky Lap</span><span class="sign__tagline">Loop Twice, Gain Extra Spin</span></div>
    </div>
  </section>

  <section class="banner banner--rectangle" aria-label="Banner 500 by 400">
    <div class="sign">
      <svg class="sign__shape" viewBox="0 0 100 100" preserveAspectRatio="none"><use href="#neon-diamond"/></svg>
      <div class="sign__text"><span class="sign__title">Lucky Lap</span><span class="sign__tagline">Loop Twice, Gain Extra Spin</span></div>
    </div>
    <span class="network-name">KVR</span>
  </section>

  <section class="banner banner--square" aria-label="Banner 447 by 426">
    <div class="sign">
      <svg class="sign__shape" viewBox="0 0 100 100" preserveAspectRatio="none"><use href="#neon-diamond"/></svg>
      <div class="sign__text"><span class="sign__title">Lucky Lap</span><span class="sign__tagline">Loop Twice, Gain Extra Spin</span></div>
    </div>
    <span class="network-name">KVR</span>
  </section>

  <section class="banner banner--small" aria-label="Banner 199 by 129">
    <div class="sign">
      <svg class="sign__shape" viewBox="0 0 100 100" preserveAspectRatio="none"><use href="#neon-diamond"/></svg>
      <div class="sign__text"><span class="sign__title">Lucky Lap</span><span class="sign__tagline">Loop Twice, Gain Extra Spin</span></div>
    </div>
    <span class="network-name">KVR</span>
  </section>

  <section class="banner banner--strip" aria-label="Banner 460 by 60">
    <div class="sign">
      <svg class="sign__shape" viewBox="0 0 100 100" preserveAspectRatio="none"><use href="#neon-diamond"/></svg>
      <div class="sign__text"><span class="sign__title">Lucky Lap</span><span class="sign__tagline">Loop Twice, Gain Extra Spin</span></div>
    </div>
    <span class="network-name">KVR</span>
  </section>
</main>
</body>
</html>
```